Business card design for sports medicine and athlete care clinic.

We need a bold, solid business card design for our practitioners to stand out. We treat overuse & sports-related injuries and provide post-operative rehabilitation. Our specialisations include chronic conditions, men’s health, nutrition & musculoskeletal disorders (MSDs). All brand collateral in terms of fonts, logo and colour palette to be provided.

Target Market(s)

Athletes (professional and amateur), sportspeople, predominantly male

Industry/Entity Type

Health And Wellness

Contact Information for Business Card

The front of the card should be white with dark blue text the back dark blue with white text. The logo should be top-left. The business name should be horizontal and right of the logo. The tagline should be directly below centred on the back of the card (see top-banner.png and bottom-banner.png)

Font styles to use
Sans Serif

Colors
0355a3
0293ce
3176b5
ffffff
85acd3

Requirements
Nice to have
• Diagonal and/or horizontal line elements between logo and practitioner details and/or bottom corner of card (see slide.png and tag-bg.png).

```html
<!DOCTYPE html>
<html lang="en">
<head>
<meta charset="utf-8">
<title>The Stride Collective – Business Card</title>
<link href="https://fonts.googleapis.com/css2?family=Montserrat:wght@500;600;700;800&display=swap" rel="stylesheet">
<style>
  :root {
    --navy: #1b1c57;
    --navy-deep: #16174a;
    --sky: #0293ce;
    --mid-blue: #3176b5;
    --pale-blue: #85acd3;
    --white: #ffffff;
    --stage: #2a2a2c;
    --ink: #1b1c57;
  }
  * { margin: 0; padding: 0; box-sizing: border-box; }
  html, body {
    width: 1200px; height: 900px; overflow: hidden;
    background: var(--stage);
    font-family: "Montserrat", sans-serif;
  }
  .stage { position: relative; width: 1200px; height: 900px; }

  .card {
    position: absolute; left: 250px; width: 700px; height: 400px;
    border-radius: 22px; overflow: hidden;
  }

  /* Back of card */
  .card-back { top: 35px; background: var(--navy); color: var(--white); }
  .back-brand {
    position: absolute; inset: 0;
    display: flex; flex-direction: column; align-items: center; justify-content: center;
    gap: 14px;
  }
  .back-mark {
    width: 70px; height: 70px; border-radius: 50%; background: var(--sky);
  }
  .back-name { font-size: 40px; font-weight: 800; letter-spacing: 0.5px; }
  .back-tagline { font-size: 15px; font-weight: 500; letter-spacing: 1px; }

  /* Front of card */
  .card-front { top: 465px; background: var(--white); color: var(--ink); }
  .front-header {
    position: absolute; left: 40px; top: 38px;
    display: flex; align-items: center; gap: 18px;
  }
  .front-mark { width: 62px; height: 62px; border-radius: 50%; background: var(--sky); flex: none; }
  .front-name { font-size: 33px; font-weight: 800; line-height: 1.1; }
  .front-tagline { font-size: 17px; font-weight: 600; font-style: italic; color: var(--sky); margin-top: 4px; }

  .divider {
    position: absolute; left: 40px; right: 40px; top: 150px;
    height: 1.5px; background: var(--navy);
  }

  .address {
    position: absolute; right: 40px; top: 168px;
    text-align: right; font-size: 15px; font-weight: 600; line-height: 1.45;
    display: flex; gap: 10px; align-items: flex-start;
  }
  .icon-bubble {
    width: 22px; height: 22px; border-radius: 50%; background: var(--sky);
    display: inline-flex; align-items: center; justify-content: center; flex: none;
  }

  .person { position: absolute; left: 40px; top: 180px; }
  .person-name { font-size: 26px; font-weight: 800; }
  .person-role { font-size: 17px; font-weight: 600; color: var(--sky); margin-top: 2px; }
  .person-rule { width: 230px; height: 1.5px; background: var(--navy); margin: 10px 0 10px; }
  .contact-list { list-style: none; }
  .contact-list li {
    display: flex; align-items: center; gap: 12px;
    font-size: 16px; font-weight: 600; margin-bottom: 8px;
  }

  .footer-band {
    position: absolute; left: 0; right: 0; bottom: 0; height: 56px;
    background: var(--navy);
    clip-path: polygon(300px 0, 100% 0, 100% 100%, 250px 100%);
    color: var(--white);
    display: flex; align-items: center; justify-content: flex-end; gap: 12px;
    padding-right: 34px; font-size: 16px; font-weight: 600;
  }
  .social-dot { width: 18px; height: 18px; border-radius: 50%; border: 2px solid var(--white); }
</style>
</head>
<body>
<main class="stage">

  <section class="card card-back" aria-label="Back of business card">
    <div class="back-brand">
      <span class="back-mark"></span>
      <h1 class="back-name">The Stride Collective</h1>
      <p class="back-tagline">Sports medicine and athlete care</p>
    </div>
  </section>

  <section class="card card-front" aria-label="Front of business card">
    <header class="front-header">
      <span class="front-mark"></span>
      <div>
        <h2 class="front-name">The Stride Collective</h2>
        <p class="front-tagline">Sports medicine and athlete care</p>
      </div>
    </header>

    <div class="divider"></div>

    <address class="address" style="font-style:normal">
      <span>18 Harbour Street<br>Suite 210, Lakeview<br>MI 49000</span>
      <span class="icon-bubble">
        <svg width="12" height="14" viewBox="0 0 12 14"><path d="M6 1a4.5 4.5 0 0 0-4.5 4.5C1.5 9 6 13 6 13s4.5-4 4.5-7.5A4.5 4.5 0 0 0 6 1z" fill="#fff"/><circle cx="6" cy="5.5" r="1.6" fill="#0293ce"/></svg>
      </span>
    </address>

    <div class="person">
      <h3 class="person-name">Mark Ellison</h3>
      <p class="person-role">Managing Director</p>
      <div class="person-rule"></div>
      <ul class="contact-list">
        <li><span class="icon-bubble"><svg width="10" height="13" viewBox="0 0 10 13"><rect x="1" y="1" width="8" height="11" rx="1.5" fill="none" stroke="#fff" stroke-width="1.5"/><circle cx="5" cy="10" r="0.8" fill="#fff"/></svg></span>555-014-2620</li>
        <li><span class="icon-bubble"><svg width="12" height="12" viewBox="0 0 12 12"><path d="M2.5 1.5l2 2-1 1.5c.8 1.5 1.8 2.5 3.3 3.3l1.5-1 2 2-1.3 1.5C5.5 10.5 1.5 6.5 1 2.8z" fill="#fff"/></svg></span>555-014-2620</li>
        <li><span class="icon-bubble"><svg width="13" height="10" viewBox="0 0 13 10"><rect x="1" y="1" width="11" height="8" rx="1" fill="none" stroke="#fff" stroke-width="1.3"/><path d="M1 1.5l5.5 4 5.5-4" fill="none" stroke="#fff" stroke-width="1.3"/></svg></span>mark@stridecollective.com</li>
      </ul>
    </div>

    <footer class="footer-band">
      <span class="social-dot"></span>
      <span>StrideCollectiveAU</span>
      <svg width="18" height="18" viewBox="0 0 18 18" aria-hidden="true"><circle cx="9" cy="9" r="7.5" fill="none" stroke="#fff" stroke-width="1.5"/><ellipse cx="9" cy="9" rx="3.2" ry="7.5" fill="none" stroke="#fff" stroke-width="1.3"/><path d="M1.5 9h15" stroke="#fff" stroke-width="1.3"/></svg>
      <span>stridecollective.com.au</span>
    </footer>
  </section>

</main>
</body>
</html>
```